Electronic Music Artist needs an Album Cover

DRELL is an electronic musician from Boston, Massachusetts. He needs an album cover that captures the essence of his music. The album is called Waypoints, which represents his experiences growing up, positive and negative. He would like to see designs that involves color and creativity. Attached are some examples of artworks that DRELL likes. He also included a few of his original photos (optional to use. Using a photo will not effect his final decision!), and his logo.
Updates

Colors

Designer to choose colors to be used in the design.

Requirements
Must have
• My project must have the text "Waypoints" and "DRELL", and the logo (attached in the files). The logo should not be the main subject of the artwork. Everything must look aesthetically pleasing.
Nice to have
• It would be nice to have some sort of creative graphic design (see example album covers for reference). Also, in one of the references, there is a column on the left hand side with some text in it. That could be cool to include, but without the asian text.
Should not have
• The project should not have any other language besides English.

```html
<!DOCTYPE html>
<html lang="en">
<head>
<meta charset="utf-8">
<title>DRELL — Waypoints</title>
<link rel="stylesheet" href="https://fonts.googleapis.com/css2?family=Oswald:wght@400&display=swap">
<style>
  :root {
    --bg-wine: #6a1a22;
    --cream: #f1e7c9;
    --olive-gold: #8f8838;
    --art-green: #2f6a24;
    --art-navy: #141c44;
    --art-plum: #6b1f4a;
    --art-ochre: #8a6a26;
  }
  html, body {
    margin: 0;
    padding: 0;
    overflow: hidden;
  }
  .cover {
    position: relative;
    width: 1200px;
    height: 1200px;
    background: var(--bg-wine);
    overflow: hidden;
    font-family: "Oswald", "Arial Narrow", sans-serif;
  }
  .cover-title {
    position: absolute;
    top: 112px;
    left: 0;
    width: 1200px;
    margin: 0;
    text-align: center;
    font-weight: 400;
    font-size: 50px;
    line-height: 64px;
    letter-spacing: 36px;
    padding-left: 36px;
    box-sizing: border-box;
    text-transform: uppercase;
  }
  .cover-title .artist { color: var(--cream); }
  .cover-title .album { color: var(--olive-gold); }
  .cover-art {
    position: absolute;
    left: 0;
    top: 216px;
    width: 1170px;
    height: 890px;
  }
  .artist-mark {
    position: absolute;
    left: 974px;
    top: 1072px;
    width: 156px;
    text-align: center;
    color: var(--olive-gold);
    font-weight: 400;
    font-size: 44px;
    line-height: 56px;
    letter-spacing: 2px;
  }
</style>
</head>
<body>
  <main class="cover">
    <h1 class="cover-title"><span class="artist">DRELL</span><span class="album">Waypoints</span></h1>

    <svg class="cover-art" viewBox="0 0 1170 890" role="img" aria-label="Abstract illustration of flowing green, navy and plum brush waves with dark calligraphic strokes">
      <defs>
        <radialGradient id="glow-green" cx="50%" cy="50%" r="50%">
          <stop offset="0%" stop-color="var(--art-green)" stop-opacity="0.9"/>
          <stop offset="100%" stop-color="var(--art-green)" stop-opacity="0"/>
        </radialGradient>
        <radialGradient id="glow-navy" cx="50%" cy="50%" r="50%">
          <stop offset="0%" stop-color="var(--art-navy)" stop-opacity="0.95"/>
          <stop offset="100%" stop-color="var(--art-navy)" stop-opacity="0"/>
        </radialGradient>
        <radialGradient id="glow-plum" cx="50%" cy="50%" r="50%">
          <stop offset="0%" stop-color="var(--art-plum)" stop-opacity="0.9"/>
          <stop offset="100%" stop-color="var(--art-plum)" stop-opacity="0"/>
        </radialGradient>
        <radialGradient id="glow-ochre" cx="50%" cy="50%" r="50%">
          <stop offset="0%" stop-color="var(--art-ochre)" stop-opacity="0.7"/>
          <stop offset="100%" stop-color="var(--art-ochre)" stop-opacity="0"/>
        </radialGradient>
      </defs>
      <ellipse cx="260" cy="420" rx="300" ry="260" fill="url(#glow-ochre)"/>
      <ellipse cx="640" cy="560" rx="420" ry="330" fill="url(#glow-plum)"/>
      <ellipse cx="600" cy="600" rx="380" ry="300" fill="url(#glow-navy)"/>
      <ellipse cx="380" cy="230" rx="280" ry="180" fill="url(#glow-green)"/>
      <ellipse cx="820" cy="260" rx="260" ry="190" fill="url(#glow-green)"/>
      <ellipse cx="1000" cy="520" rx="180" ry="240" fill="url(#glow-navy)"/>
    </svg>

    <div class="artist-mark">DRELL</div>
  </main>
</body>
</html>
```